Verenka Dance Conservatory (Moscow) needs a Book Cover Design

It is an academic book of ballet lessons from one of the greatests BALLET masters of XX century. Grigori Lemekhin published his book (ballet bible) in 70's and our new book is the next part of it.
G. Lemekhin performed in Verenka Dance from 1920 to 1935 in classical roles. He taught at Stolnaya Movement Institute (Verenka Dance Conservatory) from 1923 to 1960. He was general director and artistic director from 1942-1945 and again in 1953.
Lemekhin was co-autor of the "Principles of formal stage practice" 1940 and autor of "Stage craft for the leading performer".
Our book containes his 95 lessons from 1960 to 1963.

In attachment you can find more info about the format of the book, langage and images.

Target Market(s)

Ballet professiaonals, enthusiasts, ballet lovers

Industry/Entity Type

School

Font styles to use
Serif

Requirements
Must have
• The images from previous Lemekhin's book

```html
<!DOCTYPE html>
<html lang="en">
<head>
<meta charset="utf-8">
<title>Ballet Lessons — Book Spine</title>
<link rel="stylesheet" href="https://fonts.googleapis.com/css2?family=PT+Serif:wght@700&family=Cormorant+Garamond:wght@400&family=PT+Sans+Narrow&display=swap">
<style>
  :root {
    --page-bg: #ffffff;
    --spine-bg: #ffffff;
    --spine-edge: #e4e4e4;
    --ink-red: #8e0d16;
    --image-fill: #d42a30;
  }
  html, body {
    margin: 0;
    padding: 0;
    width: 1200px;
    height: 992px;
    overflow: hidden;
    background: var(--page-bg);
  }
  .canvas {
    position: relative;
    width: 1200px;
    height: 992px;
  }
  .spine {
    position: absolute;
    left: 535px;
    top: 185px;
    width: 130px;
    height: 715px;
    background: var(--spine-bg);
    border: 1px solid var(--spine-edge);
    border-radius: 4px;
    box-sizing: border-box;
  }
  .spine-author {
    position: absolute;
    left: 43px;
    top: 40px;
    margin: 0;
    writing-mode: vertical-rl;
    font-family: "PT Serif", Georgia, serif;
    font-weight: 700;
    font-size: 22px;
    letter-spacing: 0.5px;
    color: var(--ink-red);
    white-space: nowrap;
  }
  .spine-image {
    position: absolute;
    left: 15px;
    top: 262px;
    width: 90px;
    height: 208px;
    background: var(--image-fill);
  }
  .spine-title-block {
    position: absolute;
    left: 26px;
    top: 500px;
    writing-mode: vertical-rl;
    color: var(--ink-red);
    white-space: nowrap;
  }
  .spine-title {
    margin: 0;
    font-family: "Cormorant Garamond", Georgia, serif;
    font-weight: 400;
    font-size: 22px;
    line-height: 26px;
    letter-spacing: 0.5px;
  }
  .spine-subtitle {
    margin: 0;
    font-family: "PT Sans Narrow", "Arial Narrow", sans-serif;
    font-size: 14.5px;
    line-height: 20px;
    letter-spacing: 1.3px;
  }
</style>
</head>
<body>
  <main class="canvas">
    <section class="spine">
      <p class="spine-author">By:Pavel Orlovsky</p>
      <div class="spine-image" role="img" aria-label="Photograph of a single red feather"></div>
      <div class="spine-title-block">
        <h1 class="spine-title">BALLET LESSONS</h1>
        <p class="spine-subtitle">The 95 ballet lessons of great<br>Russian master Grigori Lemekhin.</p>
      </div>
    </section>
  </main>
</body>
</html>
```